Rental Equipment Flyer

Summit Heater Leasing. 833-584-1967. www.summitheaterleasing.example
Flyer for Rental boilers, Rental DA tank, Rental water softeners.

Please include a partnered with section: Harbor Steam & Thermal, LLC space and include Harbors logo with 866-419-5382. Logo Attached.

```html
<!DOCTYPE html>
<html lang="en">
<head>
<meta charset="utf-8">
<title>Summit Heater Leasing – Rental Equipment Flyer</title>
<link rel="stylesheet" href="https://fonts.googleapis.com/css2?family=Oswald:wght@500;600&display=swap">
<style>
  :root {
    --mat: #b7b7b7;
    --paper: #ffffff;
    --brand-orange: #ec5f22;
    --frame-orange: #fb8005;
    --brand-blue: #0066ad;
    --sky-blue: #1f9ee0;
    --logo-blue: #1565b0;
    --ink: #1f1f1f;
    --gold: #d6b56c;
  }
  html, body {
    margin: 0;
    padding: 0;
    width: 875px;
    height: 1200px;
    overflow: hidden;
    background: var(--mat);
  }
  .flyer {
    position: relative;
    width: 875px;
    height: 1200px;
    font-family: "Oswald", "Arial Narrow", sans-serif;
  }
  .flyer-shapes {
    position: absolute;
    inset: 0;
    width: 875px;
    height: 1200px;
  }
  .text { position: absolute; margin: 0; line-height: 1; color: var(--paper); font-weight: 500; white-space: nowrap; }
  .brand-name {
    left: 124px; top: 150px;
    font-size: 34px; line-height: 1.1;
    color: var(--logo-blue);
    white-space: normal; width: 200px;
  }
  .web-label { left: 125px; top: 318px; font-size: 32px; }
  .web-url { left: 125px; top: 362px; font-size: 26px; }
  .call-label { left: 127px; top: 430px; font-size: 26px; }
  .call-number { left: 125px; top: 468px; font-size: 52px; font-weight: 600; letter-spacing: -1px; }
  .service {
    top: 920px; width: 200px; font-size: 25px; text-align: center; line-height: 1.05;
    white-space: normal;
  }
  .service-boilers { left: 140px; }
  .service-da { left: 376px; }
  .service-softeners { left: 599px; }
  .partner-name {
    left: 172px; top: 1037px;
    font-size: 24px; color: var(--ink);
  }
  .partner-number { left: 528px; top: 1040px; font-size: 46px; font-weight: 600; letter-spacing: -1px; }
</style>
</head>
<body>
<div class="flyer">
  <svg class="flyer-shapes" viewBox="0 0 1652 2265" preserveAspectRatio="none" aria-hidden="false">
    <defs>
      <linearGradient id="machineryTone" x1="0" y1="0" x2="1" y2="0.4">
        <stop offset="0" stop-color="#b9693f"/>
        <stop offset="0.35" stop-color="#9a6a55"/>
        <stop offset="0.55" stop-color="#1e5aa8"/>
        <stop offset="0.8" stop-color="#3a78c0"/>
        <stop offset="1" stop-color="#c27a4c"/>
      </linearGradient>
      <linearGradient id="tankTone" x1="0" y1="0" x2="1" y2="1">
        <stop offset="0" stop-color="#c9c9c6"/>
        <stop offset="0.5" stop-color="#e8e4dc"/>
        <stop offset="1" stop-color="#b8b3a6"/>
      </linearGradient>
      <linearGradient id="siloTone" x1="0" y1="0" x2="0" y2="1">
        <stop offset="0" stop-color="#7f9a52"/>
        <stop offset="0.3" stop-color="#5e8fb8"/>
        <stop offset="0.7" stop-color="#2f5d7a"/>
        <stop offset="1" stop-color="#6c8fa6"/>
      </linearGradient>
      <linearGradient id="filterTone" x1="0" y1="0" x2="1" y2="1">
        <stop offset="0" stop-color="#eeeeee"/>
        <stop offset="0.6" stop-color="#dedede"/>
        <stop offset="1" stop-color="#f4f4f4"/>
      </linearGradient>
      <symbol id="phoneIcon" viewBox="0 0 24 24">
        <path d="M6.6 10.8c1.4 2.8 3.8 5.1 6.6 6.6l2.2-2.2c.3-.3.7-.4 1-.2 1.1.4 2.3.6 3.6.6.6 0 1 .4 1 1V20c0 .6-.4 1-1 1C10.6 21 3 13.4 3 4c0-.6.4-1 1-1h3.5c.6 0 1 .4 1 1 0 1.3.2 2.5.6 3.6.1.3 0 .7-.2 1z"/>
        <path d="M14 3.2a7.5 7.5 0 0 1 6.8 6.8M14 6.4a4.5 4.5 0 0 1 3.6 3.6" fill="none" stroke-width="1.8" stroke-linecap="round" stroke="currentColor"/>
      </symbol>
    </defs>

    <rect class="paper" x="178" y="160" width="1296" height="1945" fill="var(--paper)"/>

    <polygon role="img" aria-label="Boiler room pipework with valve wheel and pressure gauge"
      points="560,160 1474,160 1474,980 900,980 755,518" fill="url(#machineryTone)"/>

    <polygon class="service-band" points="178,980 1338,980 1474,1205 1474,1893 178,1893" fill="var(--brand-blue)"/>

    <polygon class="contact-panel" points="178,518 873,518 1172,1080 178,1080" fill="var(--brand-orange)"/>
    <polyline points="178,548 853,548 1122,1050 178,1050" fill="none" stroke="var(--paper)" stroke-width="2.5"/>

    <path d="M178,800 H563 A39,39 0 0 1 563,878 H178 Z" fill="var(--sky-blue)"/>
    <circle cx="563" cy="838" r="36" fill="var(--paper)"/>
    <use href="#phoneIcon" x="540" y="815" width="46" height="46" fill="var(--brand-orange)" color="var(--brand-orange)"/>

    <line x1="331" y1="1080" x2="331" y2="1172" stroke="var(--paper)" stroke-width="3"/>
    <line x1="331" y1="1122" x2="1425" y2="1122" stroke="var(--paper)" stroke-width="3"/>
    <line x1="578" y1="1437" x2="625" y2="1437" stroke="var(--paper)" stroke-width="3"/>
    <line x1="1030" y1="1437" x2="1070" y2="1437" stroke="var(--paper)" stroke-width="3"/>

    <polygon class="card-frame" points="178,1173 520,1173 642,1718 237,1718 178,1450" fill="var(--frame-orange)"/>
    <polygon role="img" aria-label="Row of stainless steel rental boiler tanks"
      points="178,1210 500,1210 607,1683 255,1683 178,1350" fill="url(#tankTone)"/>

    <polygon class="card-frame" points="567,1173 972,1173 1095,1718 690,1718" fill="var(--frame-orange)"/>
    <polygon role="img" aria-label="Blue steel storage tanks reflected in water"
      points="603,1210 955,1210 1060,1683 707,1683" fill="url(#siloTone)"/>

    <polygon class="card-frame" points="1010,1173 1416,1173 1474,1440 1474,1718 1132,1718" fill="var(--frame-orange)"/>
    <polygon role="img" aria-label="Water softener filter cartridge beside glasses of water"
      points="1045,1210 1396,1210 1474,1540 1474,1683 1150,1683" fill="url(#filterTone)"/>

    <polygon points="880,1893 905,1893 748,2105 722,2105" fill="var(--brand-blue)"/>
    <polygon class="partner-band" points="905,1893 1474,1893 1474,2105 748,2105" fill="var(--brand-orange)"/>
    <use href="#phoneIcon" x="900" y="1976" width="64" height="64" fill="var(--paper)" color="var(--paper)"/>

    <circle cx="268" cy="2003" r="36" fill="var(--gold)"/>
  </svg>

  <p class="text brand-name">Summit Heater Leasing</p>

  <p class="text web-label">Website</p>
  <p class="text web-url">www.summitheaterleasing.example</p>
  <p class="text call-label">Call Us</p>
  <p class="text call-number">833-584-1967</p>

  <p class="text service service-boilers">Rental Boilers</p>
  <p class="text service service-da">Rental DA tank</p>
  <p class="text service service-softeners">Rental Water Softeners</p>

  <p class="text partner-name">Harbor Steam &amp; Thermal</p>
  <p class="text partner-number">866-419-5382</p>
</div>
</body>
</html>
```